Dental 2 practice oudoor signs

I need 2 high quality practice signs designed
sign 1 ( 1.6m high by 0.8m wide)
sign 2 ( sign 1.05m high by 0.80m wide)

I had sign 1 displayed before which i have attached but it doest look as professional now. We are a multi award winning dental clinic. Both signs will be printed on dibond and be at a 45 degree to each other so that the person walking past will only see one sign, unless he walks in the opposite direction. Here is the brief of sign 1 and sign 2 but feel free to diverse away from the brief and do something differet

Sign 1
Marlow Dental, Implant & Orthodontic Centre

Size of sign 1600 Height by 800 WIde
website: www.marlowdentalclinic.example
Sign text

Multi-Award Winning
Centre of Excellence

Dental Implants from £ 38.23/mo
Clearvex Braces from £ 29.23/mo
Dental Veneers from £11.13/mo
Smile Makeovers from £34.13/mo
Specialist Orthodontics from £29.23/mo
Facial Aesthetics from £22.16/mo

020 7915 3608
www.marlowdentalclinic.example

Each of the above treatements should be also represented graphically so the sign is very colorful and draws your attention but gives a quality feel about it
You can find graphics wherever you need to, to advertise the services

Sign 2.
Use any detail you wish from sign 1 but i definately want
Multi-Award Winning on both signs

Target Market(s)

Passers by who are driving past dental practice or pedestrians who are walking past practice

Industry/Entity Type

Dental Clinic

Colors

Designer to choose colors to be used in the design.

Requirements
Must have
• See brief

```html
<!DOCTYPE html>
<html lang="en">
<head>
<meta charset="utf-8">
<title>Marlow Dental – Practice Sign</title>
<link rel="stylesheet" href="https://fonts.googleapis.com/css2?family=Jost:wght@400;500;700&family=Oswald:wght@600&display=swap">
<style>
  :root {
    --navy: #0f2b5c;
    --navy-deep: #0b2350;
    --blue: #2c6dc2;
    --cyan: #18c0f2;
    --grey: #575757;
    --gold: #d9aa3c;
    --gold-light: #f3d488;
    --silver: #e4e4e6;
    --white: #ffffff;
    --backdrop: #eeeeee;
  }
  * { margin: 0; padding: 0; box-sizing: border-box; }
  html, body {
    width: 991px; height: 1200px; overflow: hidden;
    background: var(--backdrop);
  }
  .canvas { position: relative; width: 991px; height: 1200px; }
  .sign {
    position: absolute; left: 49px; top: 15px;
    width: 924px; height: 1212px;
    transform: scale(0.965); transform-origin: top left;
    background: var(--white); overflow: hidden;
    font-family: "Jost", "Century Gothic", sans-serif;
  }
  .sign-wave { position: absolute; inset: 0; width: 924px; height: 1212px; }
  .brand-name {
    position: absolute; top: 205px; left: 0; width: 100%;
    text-align: center; font-size: 48px; font-weight: 500;
    color: var(--navy); letter-spacing: 5px; text-transform: uppercase;
    line-height: 1;
  }
  .headline {
    position: absolute; top: 405px; left: 0; width: 100%;
    text-align: center; font-size: 90px; font-weight: 700;
    color: var(--navy); line-height: 1; letter-spacing: 1px;
  }
  .subline {
    position: absolute; top: 505px; left: 0; width: 100%;
    text-align: center; font-size: 40px; font-weight: 400;
    color: var(--grey); line-height: 1; letter-spacing: 0.5px;
  }
  .badge { position: absolute; }
  .badge-award { left: 155px; top: 615px; width: 285px; height: 275px; }
  .badge-excellence { left: 488px; top: 617px; width: 265px; height: 265px; }
  .badge-label {
    position: absolute; text-align: center; color: var(--navy);
    line-height: 1; text-transform: uppercase;
  }
  .award-label { left: 177px; width: 240px; top: 718px; }
  .excellence-label { left: 500px; width: 241px; top: 762px; }
  .badge-label .small { display: block; font-size: 21px; font-weight: 400; color: var(--grey); }
  .badge-label .big { display: block; font-size: 44px; font-weight: 700; margin: 2px 0; }
  .excellence-label .big { font-size: 38px; margin: 0 0 2px; }
  .excellence-label .small { font-size: 18px; color: var(--navy); }
  .phone {
    position: absolute; right: 54px; top: 1060px;
    font-family: "Oswald", "Arial Narrow", sans-serif;
    font-size: 100px; font-weight: 600; color: var(--white);
    line-height: 1; letter-spacing: 1px;
  }
  .website {
    position: absolute; right: 74px; top: 1164px;
    font-size: 30px; font-weight: 400; color: var(--white); line-height: 1;
  }
  .website strong { font-weight: 700; }
</style>
</head>
<body>
<div class="canvas">
  <div class="sign">
    <svg class="sign-wave" viewBox="0 0 924 1212" aria-hidden="true">
      <defs>
        <linearGradient id="waveNavy" x1="0" y1="0" x2="0.3" y2="1">
          <stop offset="0" stop-color="#2c6dc2"/>
          <stop offset="1" stop-color="#0b2350"/>
        </linearGradient>
      </defs>
      <path d="M0,1185 C130,1060 320,1000 560,985 C790,970 905,890 924,655 L924,1212 L0,1212Z" fill="var(--cyan)"/>
      <path d="M0,1200 C125,1085 310,1022 560,1008 C795,993 908,915 924,730 L924,1212 L0,1212Z" fill="var(--white)"/>
      <path d="M0,1212 C120,1110 300,1045 560,1030 C800,1015 910,940 924,800 L924,1212Z" fill="url(#waveNavy)"/>
    </svg>

    <div class="brand-name">Marlow Dental Surgery</div>

    <h1 class="headline">MARLOW DENTAL</h1>
    <p class="subline">IMPLANT &amp; ORTHODONTIC CENTRE</p>

    <svg class="badge badge-award" viewBox="0 0 285 275" role="img" aria-label="Gold laurel wreath award badge">
      <defs>
        <radialGradient id="goldFill" cx="0.5" cy="0.5" r="0.5">
          <stop offset="0.74" stop-color="var(--white)"/>
          <stop offset="0.8" stop-color="var(--gold-light)"/>
          <stop offset="1" stop-color="var(--gold)"/>
        </radialGradient>
      </defs>
      <circle cx="142" cy="150" r="122" fill="url(#goldFill)"/>
    </svg>
    <div class="badge-label award-label">
      <span class="small">Multi</span>
      <span class="big">Award</span>
      <span class="small">Winning</span>
    </div>

    <svg class="badge badge-excellence" viewBox="0 0 265 265" role="img" aria-label="Round centre of excellence certificate badge">
      <defs>
        <radialGradient id="silverFill" cx="0.4" cy="0.35" r="0.7">
          <stop offset="0" stop-color="var(--white)"/>
          <stop offset="1" stop-color="var(--silver)"/>
        </radialGradient>
      </defs>
      <circle cx="132.5" cy="132.5" r="128" fill="url(#silverFill)" stroke="var(--gold)" stroke-width="5"/>
    </svg>
    <div class="badge-label excellence-label">
      <span class="big">Centre</span>
      <span class="small">of Excellence</span>
    </div>

    <div class="phone">020 7915 3608</div>
    <div class="website">www.<strong>marlowdentalclinic</strong>.example</div>
  </div>
</div>
</body>
</html>
```